Book cover design for the book titled "Quieter Under Lanterns."

create a book cover. The book title is, "Quieter Under Lanterns: A Ledger of Harbour Songs Across Mild Winters." The purpose of the book is to create awareness of how childhood trauma is impacting 7 out of 10 adults in the world today and that two-thirds of children will experience neglect and or abuse before their 18th birthday. One victim described that his mental and physical illness resulting from childhood trauma felt like he wa being pulled to the ground, that the force was "quieter under lanterns." The design should be clean and simple and communicate a crisis.

```html
<!DOCTYPE html>
<html lang="en">
<head>
<meta charset="utf-8">
<title>Quieter Under Lanterns — Book Cover</title>
<link href="https://fonts.googleapis.com/css2?family=Bebas+Neue&family=Roboto:wght@500&display=swap" rel="stylesheet">
<style>
  :root {
    --page-bg: #161616;
    --cover-bg: #dddbe0;
    --ink: #2a2729;
    --title-red: #9e2141;
    --title-red-light: #c95670;
    --rule: #4a4648;
    --figure-light: #cfc8d2;
    --figure-mid: #9d92a0;
  }
  * { margin: 0; padding: 0; box-sizing: border-box; }
  html, body {
    width: 1200px;
    height: 1200px;
    overflow: hidden;
    background: var(--page-bg);
  }
  .cover {
    position: absolute;
    left: 211px;
    top: 50px;
    width: 777px;
    height: 1100px;
    background: var(--cover-bg);
    text-align: center;
    box-shadow: 0 10px 40px rgba(0,0,0,0.5);
  }
  .cover h1 { font-weight: normal; }
  .title-lead {
    position: absolute;
    top: 80px;
    left: 0;
    width: 100%;
    font-family: "Roboto", sans-serif;
    font-weight: 500;
    font-size: 74px;
    line-height: 1;
    color: var(--ink);
  }
  .title-main {
    position: absolute;
    top: 156px;
    left: 83px;
    width: 611px;
    height: 206px;
    overflow: visible;
  }
  .title-main text {
    font-family: "Bebas Neue", sans-serif;
    font-size: 276px;
  }
  .title-rule {
    position: absolute;
    top: 374px;
    left: 189px;
    width: 398px;
    height: 2px;
    background: var(--rule);
  }
  .subtitle {
    position: absolute;
    top: 393px;
    left: 0;
    width: 100%;
    font-family: "Roboto", sans-serif;
    font-weight: 500;
    font-size: 32px;
    line-height: 39px;
    color: var(--ink);
    text-transform: uppercase;
  }
  .cover-art {
    position: absolute;
    left: 183px;
    top: 529px;
    width: 511px;
    height: 414px;
    border-radius: 46% 40% 12% 20%;
    background: radial-gradient(ellipse at 45% 55%, var(--figure-mid) 0%, var(--figure-light) 70%, var(--cover-bg) 100%);
  }
  .author {
    position: absolute;
    top: 1008px;
    left: 0;
    width: 100%;
    font-family: "Roboto", sans-serif;
    font-weight: 500;
    font-size: 36px;
    letter-spacing: 8px;
    color: var(--ink);
  }
</style>
</head>
<body>
  <main class="cover">
    <h1>
      <span class="title-lead">QUIETER UNDER</span>
      <svg class="title-main" viewBox="0 0 611 206" aria-label="Lanterns">
        <defs>
          <radialGradient id="title-glow" cx="50%" cy="70%" r="60%">
            <stop offset="0%" stop-color="#c95670"/>
            <stop offset="100%" stop-color="#9e2141"/>
          </radialGradient>
        </defs>
        <text x="305.5" y="196" text-anchor="middle" textLength="607" lengthAdjust="spacingAndGlyphs" fill="url(#title-glow)">LANTERNS</text>
      </svg>
    </h1>
    <div class="title-rule"></div>
    <p class="subtitle">A Ledger of Harbour Songs<br>Across Mild Winters</p>
    <div class="cover-art" role="img" aria-label="Illustration of a child sitting on the floor hugging their knees with head bowed"></div>
    <p class="author">AUTHOR NAME</p>
  </main>
</body>
</html>
```